Stretch on the Green with Mira

I want to advertise my Stretch on the Green classes for Summer. Classes are outside at the lovely local park. Holloway field. 83 Marangi St. Sandringham.
Classes are for beginners to advance levels.
Classes start Monday, October 17th.
Monday 6pm Beginners
Tuesday 6pm Intermediate
Thursday 6pm Intermediate/Advance
Saturday 9am All fitness levels
My Pilates classes are specially designed to help improve strength and flexibility but as well will also improve posture, reduce stress and develop control and endurance in the entire body.
Booking essential. Limited numbers so I can make sure the correct technique is always being followed.
For more info or to book contact details:
Mira 027358164
mira@corewithmira.net
www.corewithmira.net
$15 Per Session

Target Market(s)

Males and Females ages 35plus.

Industry/Entity Type

Fitness

Font styles to use
Sans Serif

Requirements
Must have
• My logo. Contact details. A Park that looks lovely to exercise at.
Nice to have
• Summer looking. Trees - inspiration to be exercising outside

```html
<!DOCTYPE html>
<html lang="en">
<head>
<meta charset="utf-8">
<title>Stretch on the Green with Mira – Summer Classes Flyer</title>
<link rel="stylesheet" href="https://fonts.googleapis.com/css2?family=Poppins:wght@300;400;500;600;700;800&family=Bebas+Neue&display=swap">
<style>
  :root {
    --pink: #f47fb8;
    --pink-soft: #f8a3cc;
    --pink-deep: #ec5fa4;
    --charcoal: #4a4a4c;
    --slate: #58595b;
    --grey: #8b8b8d;
    --card-grey: #7b7b7d;
    --white: #ffffff;
    --paper: #ffffff;
  }
  * { box-sizing: border-box; margin: 0; padding: 0; }
  html, body {
    width: 1200px; height: 2400px; overflow: hidden;
    background: var(--paper);
    font-family: "Poppins", Arial, sans-serif;
  }
  .flyer {
    position: absolute; left: 35px; top: 468px;
    width: 942px; height: 1219px;
    transform: scale(1.2); transform-origin: 0 0;
    background: var(--white);
    overflow: hidden;
    box-shadow: 0 6px 24px rgba(0,0,0,.12);
  }
  .hero-photo {
    position: absolute; left: 0; top: 0; width: 942px; height: 525px;
    background:
      linear-gradient(90deg, var(--pink) 0%, var(--pink-soft) 35%, rgba(248,163,204,.4) 55%, rgba(248,163,204,0) 75%),
      linear-gradient(180deg, #e9b37a 0%, #b89a4e 40%, #7f8a35 70%, #5d7a2a 100%);
  }
  .brand { position: absolute; left: 45px; top: 50px; width: 350px; }
  .brand-dot {
    display: block; width: 52px; height: 52px; border-radius: 50%;
    background: var(--white); margin: 0 0 22px 150px;
  }
  .brand-name {
    color: var(--white); font-weight: 300; font-size: 27px; letter-spacing: 1px;
    white-space: nowrap;
  }
  .title-main {
    position: absolute; left: 42px; top: 180px;
    font-weight: 800; font-size: 82px; line-height: 1; color: var(--charcoal);
    letter-spacing: 1px;
  }
  .title-sub {
    position: absolute; left: 44px; top: 262px;
    font-family: "Bebas Neue", Impact, sans-serif;
    font-size: 96px; line-height: 1; color: var(--white); letter-spacing: 1px;
  }
  .tagline {
    position: absolute; left: 45px; top: 360px; width: 400px;
    font-weight: 600; font-size: 21px; line-height: 1.25; color: #3b3b3d;
  }
  .venue {
    position: absolute; left: 45px; top: 418px;
    background: var(--white); border-radius: 8px; padding: 0 10px;
    font-weight: 600; font-size: 33px; line-height: 40px; color: var(--charcoal);
    letter-spacing: .5px;
  }
  .address {
    position: absolute; left: 48px; top: 466px;
    display: flex; align-items: center; gap: 5px;
    font-weight: 600; font-size: 19px; color: var(--white);
  }
  .info-bar {
    position: absolute; left: 45px; top: 510px; width: 850px; height: 55px;
    display: flex; gap: 5px; border: 2px solid #d5d5d7; border-radius: 12px; overflow: hidden;
    background: var(--white);
  }
  .info-bar span {
    display: flex; align-items: center; padding-left: 18px;
    font-weight: 500; font-size: 23px; letter-spacing: .3px;
  }
  .info-levels { width: 425px; background: var(--grey); color: #2f2f31; }
  .info-start { flex: 1; background: var(--slate); color: var(--white); }
  .schedule { position: absolute; top: 592px; left: 45px; display: flex; gap: 27px; }
  .day-card {
    width: 158px; height: 138px; background: var(--white); border-radius: 8px;
    box-shadow: 0 3px 8px rgba(0,0,0,.18); position: relative;
  }
  .day-head {
    height: 66px; border-radius: 8px 8px 0 0; padding-top: 30px;
    text-align: center; color: var(--white); font-weight: 500; font-size: 15px;
  }
  .day-card.pink .day-head { background: var(--pink); }
  .day-card.grey .day-head { background: var(--card-grey); }
  .rings { position: absolute; left: 18px; top: -4px; display: flex; gap: 20px; }
  .rings i { display: block; width: 8px; height: 24px; border-radius: 4px; background: #2f2f31; }
  .day-level {
    height: 72px; display: flex; align-items: center; justify-content: center;
    text-align: center; font-weight: 500; font-size: 15px; line-height: 1.2; color: #3b3b3d;
  }
  .benefits-intro {
    position: absolute; left: 47px; top: 742px; z-index: 2;
    font-weight: 500; font-size: 28px; line-height: 31px; color: #333335;
  }
  .benefits-intro em { font-style: normal; color: var(--pink); display: block; }
  .price {
    position: absolute; left: 440px; top: 758px; height: 40px;
    display: flex; font-weight: 600; font-size: 32px; line-height: 40px;
  }
  .price-amount { background: var(--slate); color: var(--white); padding: 0 8px; border-radius: 6px 0 0 6px; }
  .price-unit { background: var(--pink); color: var(--white); padding: 0 10px; border-radius: 0 6px 6px 0; }
  .benefits {
    position: absolute; left: 45px; top: 812px; width: 710px; height: 206px;
    border: 2px solid var(--pink); border-radius: 14px;
    display: flex; padding-top: 25px;
  }
  .benefits::before {
    content: ""; position: absolute; left: 12px; top: -2px; width: 360px; height: 4px; background: var(--white);
  }
  .benefit {
    flex: 1; text-align: center; border-right: 1px solid #e6e6e8;
    font-weight: 500; font-size: 19px; line-height: 23px; color: #3b3b3d;
  }
  .benefit:last-child { border-right: none; }
  .benefit-icon { display: block; margin: 0 auto 10px; }
  .booking {
    position: absolute; left: 45px; top: 1034px;
    display: flex; align-items: center; gap: 14px;
  }
  .booking strong {
    font-family: "Bebas Neue", Impact, sans-serif; font-weight: 400;
    font-size: 40px; color: var(--pink); letter-spacing: .5px;
  }
  .booking span { font-weight: 500; font-size: 14px; line-height: 17px; color: #333335; width: 360px; }
  .footer {
    position: absolute; left: 0; top: 1093px; width: 942px; height: 126px;
    background: var(--slate); color: var(--white);
  }
  .footer-lead { position: absolute; left: 45px; top: 14px; font-weight: 500; font-size: 15px; }
  .contact-name { position: absolute; left: 45px; top: 34px; font-weight: 500; font-size: 24px; color: var(--pink); }
  .contact-line {
    position: absolute; display: flex; align-items: center; gap: 8px;
    font-weight: 400; font-size: 21px;
  }
  .model-photo {
    position: absolute; left: 765px; top: 630px; width: 177px; height: 589px;
    border-radius: 90px 0 0 0;
    background: linear-gradient(180deg, #f3d6cf 0%, #7a2231 28%, #6b1f2c 70%, #5a1a26 100%);
    opacity: .9;
  }
</style>
</head>
<body>
<main class="flyer">
  <div class="hero-photo" role="img" aria-label="Two women doing lunges on the grass of a sunny, tree-lined park"></div>

  <div class="brand">
    <span class="brand-dot"></span>
    <p class="brand-name">Stretch with Mira</p>
  </div>

  <h1>
    <span class="title-main">STRETCH</span>
    <span class="title-sub">ON THE GREEN</span>
  </h1>

  <p class="tagline">Summer classes are outside at the lovely local park.</p>
  <p class="venue">HOLLOWAY FIELD</p>
  <p class="address">
    <svg width="18" height="20" viewBox="0 0 18 20"><path d="M9 1a6 6 0 0 0-6 6c0 4.5 6 10 6 10s6-5.5 6-10a6 6 0 0 0-6-6z" fill="#4a4a4c"/><circle cx="9" cy="7" r="2.2" fill="#fff"/><ellipse cx="9" cy="18.5" rx="7" ry="1.3" fill="#4a4a4c"/></svg>
    83 Marangi St. Sandringham
  </p>

  <div class="info-bar">
    <span class="info-levels">BEGINNERS TO ADVANCE LEVELS</span>
    <span class="info-start">STARTS MONDAY, OCTOBER 17TH</span>
  </div>

  <section class="schedule">
    <div class="day-card pink"><div class="rings"><i></i><i></i><i></i><i></i><i></i></div><div class="day-head">MONDAY 6PM</div><div class="day-level">BEGINNERS</div></div>
    <div class="day-card grey"><div class="rings"><i></i><i></i><i></i><i></i><i></i></div><div class="day-head">TUESDAY 6PM</div><div class="day-level">INTERMEDIATE</div></div>
    <div class="day-card pink"><div class="rings"><i></i><i></i><i></i><i></i><i></i></div><div class="day-head">THURSDAY 6PM</div><div class="day-level">INTERMEDIATE<br>/ADVANCE</div></div>
    <div class="day-card grey"><div class="rings"><i></i><i></i><i></i><i></i><i></i></div><div class="day-head">SATURDAY 9AM</div><div class="day-level">ALL FITNESS<br>LEVELS</div></div>
  </section>

  <p class="benefits-intro"><em>My Pilates classes</em>are specially designed to</p>
  <p class="price"><span class="price-amount">$15</span><span class="price-unit">PER SESSION</span></p>

  <section class="benefits">
    <div class="benefit"><svg class="benefit-icon" width="70" height="70" viewBox="0 0 70 70"><path d="M8 38a27 27 0 0 1 54 0" fill="none" stroke="#f47fb8" stroke-width="2"/><circle cx="35" cy="35" r="23" fill="#4a4a4c"/><path d="M25 42c2-8 6-12 12-12 2-4 6-5 8-2l-3 3c-2 0-3 1-3 3h5c2 3 0 8-5 8z" fill="#fff"/></svg>Improve<br>Strength &amp;<br>Flexibility</div>
    <div class="benefit"><svg class="benefit-icon" width="70" height="70" viewBox="0 0 70 70"><path d="M8 38a27 27 0 0 1 54 0" fill="none" stroke="#f47fb8" stroke-width="2"/><circle cx="35" cy="35" r="23" fill="#4a4a4c"/><rect x="33" y="20" width="4" height="30" rx="2" fill="#fff"/><circle cx="35" cy="18" r="3" fill="#fff"/></svg>Improve<br>Posture</div>
    <div class="benefit"><svg class="benefit-icon" width="70" height="70" viewBox="0 0 70 70"><path d="M8 38a27 27 0 0 1 54 0" fill="none" stroke="#f47fb8" stroke-width="2"/><circle cx="35" cy="35" r="23" fill="#4a4a4c"/><circle cx="35" cy="35" r="10" fill="none" stroke="#fff" stroke-width="3"/><circle cx="35" cy="35" r="3" fill="#fff"/></svg>Reduce<br>Stress</div>
    <div class="benefit"><svg class="benefit-icon" width="70" height="70" viewBox="0 0 70 70"><path d="M8 38a27 27 0 0 1 54 0" fill="none" stroke="#f47fb8" stroke-width="2"/><circle cx="35" cy="35" r="23" fill="#4a4a4c"/><rect x="24" y="24" width="22" height="22" rx="3" fill="none" stroke="#fff" stroke-width="2.5"/><path d="M30 28v14M35 28v14M40 28v14" stroke="#fff" stroke-width="2"/></svg>Develop<br>Control</div>
    <div class="benefit"><svg class="benefit-icon" width="70" height="70" viewBox="0 0 70 70"><path d="M8 38a27 27 0 0 1 54 0" fill="none" stroke="#f47fb8" stroke-width="2"/><circle cx="35" cy="35" r="23" fill="#4a4a4c"/><circle cx="35" cy="25" r="4" fill="#fff"/><path d="M24 44h22l-5-6-3-8h-6l-3 8z" fill="#fff"/></svg>endurance<br>in the entire<br>body</div>
  </section>

  <div class="booking">
    <strong>BOOKING ESSENTIAL</strong>
    <span>Limited numbers so I can make sure the correct technique is always being followed.</span>
  </div>

  <footer class="footer">
    <p class="footer-lead">For more info or to book contact us:</p>
    <p class="contact-name">MIRA KELLAWAY</p>
    <p class="contact-line" style="left:45px; top:66px;">
      <svg width="18" height="18" viewBox="0 0 24 24"><path d="M6.6 10.8a15 15 0 0 0 6.6 6.6l2.2-2.2c.3-.3.7-.4 1-.2 1.1.4 2.3.6 3.6.6.6 0 1 .4 1 1V20c0 .6-.4 1-1 1A17 17 0 0 1 3 4c0-.6.4-1 1-1h3.5c.6 0 1 .4 1 1 0 1.300.2 2.5.6 3.6.1.3 0 .7-.2 1z" fill="#f47fb8"/></svg>
      027 358164
    </p>
    <p class="contact-line" style="left:300px; top:34px;">
      <svg width="20" height="16" viewBox="0 0 20 16"><rect x="1" y="1" width="18" height="14" rx="2" fill="#f47fb8"/><path d="M1 2l9 7 9-7" fill="none" stroke="#58595b" stroke-width="1.6"/></svg>
      mira@corewithmira.net
    </p>
    <p class="contact-line" style="left:300px; top:66px;">
      <svg width="18" height="18" viewBox="0 0 20 20"><circle cx="10" cy="10" r="8.5" fill="none" stroke="#f47fb8" stroke-width="2"/><path d="M1.5 10h17M10 1.5c-3 3-3 14 0 17M10 1.5c3 3 3 14 0 17" fill="none" stroke="#f47fb8" stroke-width="1.6"/></svg>
      www.corewithmira.net
    </p>
  </footer>

  <div class="model-photo" role="img" aria-label="Woman in maroon activewear kneeling in a lunge with arms raised overhead"></div>
</main>
</body>
</html>
```